Electrician Company Website Design

I am looking to get a website designed only. I do not need it converted ot html. I simply need the design in a psd format. I have my own team for the conversion. The website is for an electrician company called Bramblecourt electric. I have created a txt document with the project parameters and specifics. I have also uploaded their logo in all avaible formats. It's a zip file.

Number of Pages Required

1 page

```html
<!DOCTYPE html>
<html lang="en">
<head>
<meta charset="utf-8">
<title>Bramblecourt Electric</title>
<link href="https://fonts.googleapis.com/css2?family=Barlow+Condensed:wght@400;500;600&family=Barlow:wght@400;500;600&display=swap" rel="stylesheet">
<style>
:root{
  --red:#b3242b;
  --red-dark:#7d1419;
  --blue:#1464c8;
  --blue-dark:#0d4a9a;
  --ink:#1d1d1f;
  --charcoal:#2b2b2d;
  --grey:#efefef;
  --text:#444;
  --white:#fff;
}
*{box-sizing:border-box;margin:0;padding:0}
html,body{width:1200px;height:4955px;overflow:hidden;background:var(--white)}
body{font-family:"Barlow",sans-serif;color:var(--text);position:relative}
.abs{position:absolute}
.head{font-family:"Barlow Condensed",sans-serif;font-weight:600;text-transform:uppercase;letter-spacing:.5px}
.ph{position:absolute}
/* header */
.site-header{position:absolute;left:0;top:0;width:1200px;height:98px;background:var(--white);z-index:5}
.brand{position:absolute;left:92px;top:10px;width:168px;height:126px;border-radius:50%;background:var(--white);display:flex;align-items:center;justify-content:center;font-family:"Barlow Condensed",sans-serif;font-weight:600;font-size:20px;color:var(--ink);text-transform:uppercase;text-align:center;line-height:1.05;box-shadow:0 2px 8px rgba(0,0,0,.12)}
.nav{position:absolute;top:46px;left:0;font-family:"Barlow Condensed",sans-serif;font-size:15px;text-transform:uppercase;color:var(--ink)}
.nav a{position:absolute;color:inherit;text-decoration:none;white-space:nowrap}
.nav a.active{color:var(--red)}
.nav a.active::after{content:"";position:absolute;left:-6px;right:-6px;top:46px;height:4px;background:var(--red)}
.call{position:absolute;right:0;top:0;width:232px;height:98px;background:var(--red);clip-path:polygon(14% 0,100% 0,100% 100%,0 100%);color:var(--white);padding:28px 0 0 48px;font-family:"Barlow Condensed",sans-serif}
.call small{font-size:16px;display:block}
.call b{font-weight:500;font-size:22px}
/* hero */
.hero{position:absolute;top:98px;left:0;width:1200px;height:680px;background:linear-gradient(100deg,#2a2a2c 10%,#1b4d97 55%,#1466d6 100%);overflow:hidden}
.hero-frame{position:absolute;left:98px;top:172px;width:110px;height:270px;border:3px solid var(--white);border-right:none}
.hero-kicker{position:absolute;left:136px;top:220px;color:var(--white);font-family:"Barlow Condensed",sans-serif;font-size:22px;letter-spacing:2px}
.hero-title{position:absolute;left:136px;top:246px;color:var(--white);font-size:43px;line-height:48px}
.btn-red{position:absolute;background:var(--red);color:var(--white);font-family:"Barlow Condensed",sans-serif;font-size:16px;text-transform:uppercase;display:flex;align-items:center;justify-content:center}
.btn-line{position:absolute;border:2px solid var(--blue);color:var(--blue);font-family:"Barlow Condensed",sans-serif;font-weight:600;font-size:16px;text-transform:uppercase;display:flex;align-items:center;justify-content:center}
/* section titles */
.ghost{position:absolute;font-family:"Barlow Condensed",sans-serif;font-weight:600;text-transform:uppercase;color:rgba(0,0,0,.06);white-space:nowrap}
.title{position:absolute;font-family:"Barlow Condensed",sans-serif;font-weight:500;text-transform:uppercase;font-size:40px;color:var(--ink);white-space:nowrap}
.title em{font-style:normal;color:var(--red)}
.divider{position:absolute;width:130px;height:14px}
.divider::before,.divider::after{content:"";position:absolute;top:6px;width:52px;height:2px;background:var(--ink)}
.divider::before{left:0}.divider::after{right:0}
.divider i{position:absolute;left:60px;top:0;width:10px;height:14px;background:var(--blue);clip-path:polygon(60% 0,10% 58%,45% 58%,30% 100%,90% 40%,55% 40%)}
.on-dark .divider::before,.on-dark .divider::after{background:var(--white)}
.on-dark .divider i{background:var(--white)}
/* services diamonds */
.diamond{position:absolute;width:296px;height:296px;transform:rotate(45deg);outline-offset:8px}
.diamond-text{position:absolute;width:280px;text-align:center;color:var(--white)}
.diamond-text h3{font-family:"Barlow Condensed",sans-serif;font-weight:500;font-size:23px;line-height:27px;text-transform:uppercase}
.diamond-text p{font-size:13px;line-height:19px;margin-top:12px;opacity:.9}
/* body text */
.copy{position:absolute;font-size:14.5px;line-height:23px;color:var(--text)}
.loc{position:absolute;font-size:14px;font-weight:500;color:var(--ink);display:flex;align-items:center;gap:9px}
.pin{width:22px;height:22px;border-radius:50%;background:var(--blue);position:relative}
.pin::after{content:"";position:absolute;left:7px;top:7px;width:8px;height:8px;border-radius:50%;background:var(--white)}
/* gallery */
.gallery-item{position:absolute;top:2880px;width:252px;height:213px}
/* faq */
.faq{position:absolute;left:605px;width:466px;height:58px;border-bottom:1px solid #bbb;font-size:15px;color:var(--ink);display:flex;align-items:center;justify-content:space-between;padding-top:4px}
.chev{width:10px;height:10px;border-right:2px solid var(--blue);border-bottom:2px solid var(--blue);transform:rotate(45deg);margin-right:12px}
/* form */
.field{position:absolute;border:1px solid #999;font-size:12px;color:#666;padding:7px 14px}
/* footer */
.footer{position:absolute;left:0;top:4555px;width:1200px;height:400px;background:#000;color:var(--white)}
.f-col{position:absolute;top:70px;font-size:12.5px;line-height:23px;color:#ddd}
.f-col h4{font-family:"Barlow Condensed",sans-serif;font-weight:500;font-size:17px;color:var(--white);margin-bottom:10px;text-transform:uppercase}
.f-sep{position:absolute;top:10px;width:1px;height:300px;background:#2a2a2a}
.social{display:flex;gap:10px;position:absolute;left:170px;top:210px}
.social span{width:26px;height:26px;border-radius:50%;background:#2f6bd8}
</style>
</head>
<body>

<header class="site-header">
  <div class="brand">Bramblecourt<br>Electric</div>
  <nav class="nav">
    <a class="active" style="left:336px">Company</a>
    <a style="left:449px">Service Area</a>
    <a style="left:587px">Services</a>
    <a style="left:700px">Contact</a>
    <a style="left:811px">Gallery</a>
    <a style="left:913px">FAQs</a>
  </nav>
  <div class="call"><small>CALL US TODAY!</small>
    <svg width="18" height="18" viewBox="0 0 24 24" style="vertical-align:-2px"><circle cx="12" cy="12" r="12" fill="#fff"/><path d="M8 6l2 0 1 3-1.5 1a8 8 0 0 0 4.5 4.5l1-1.5 3 1v2c0 1-1 2-2 2A11 11 0 0 1 6 8c0-1 1-2 2-2z" fill="#b3242b"/></svg>
    <b>555 214 7730</b></div>
</header>

<section class="hero">
  <div class="hero-frame"></div>
  <div class="hero-kicker">BRAMBLECOURT ELECTRIC</div>
  <h1 class="hero-title head">Commercial and<br>Residential Electrical</h1>
  <div class="btn-red" style="left:140px;top:357px;width:160px;height:45px">Contact Us →</div>
  <div class="ph" style="left:732px;top:90px;width:380px;height:260px;background:#1a73e8"></div>
  <div class="ph" role="img" aria-label="Smiling electrician in hard hat working on a wiring panel" style="left:575px;top:104px;width:530px;height:580px;background:linear-gradient(135deg,#9aa3ad,#c9b98a 55%,#5a6b3a);border-radius:0 0 0 0"></div>
  <svg class="ph" style="left:0;top:545px" width="1200" height="135"><polygon points="0,120 0,25 580,120" fill="#9c1d22"/><polygon points="0,0 0,20 580,110 575,120" fill="#b3242b"/><polygon points="0,135 0,120 580,120 1200,60 1200,135" fill="#fff"/></svg>
</section>

<section class="services">
  <div class="ghost" style="left:370px;top:815px;font-size:90px">What we do</div>
  <div class="ph" style="left:565px;top:818px;width:70px;height:30px;background:var(--blue-dark);clip-path:polygon(0 0,50% 60%,100% 0,50% 100%)"></div>
  <div class="title" style="left:457px;top:845px;font-size:40px">Services <em>Provide</em></div>
  <div class="divider" style="left:535px;top:893px"><i></i></div>

  <div class="diamond" style="left:117px;top:997px;background:linear-gradient(135deg,#2a7de0,#0e4fae);outline:1px solid var(--blue)" role="img" aria-label="Commercial electrical workers, blue tinted"></div>
  <div class="diamond-text" style="left:125px;top:1105px"><h3>Commerical<br>Electrical Services</h3><p>Lorem Ipsum is simply dummy text of the printing and typesetting industry.</p></div>

  <div class="diamond" style="left:453px;top:997px;background:linear-gradient(135deg,#b3242b,#6a1216);outline:1px solid var(--red);box-shadow:0 10px 40px rgba(179,36,43,.35)" role="img" aria-label="Residential electricians, red tinted"></div>
  <div class="diamond-text" style="left:461px;top:1105px"><h3>Residential<br>Electrical Services</h3><p>Lorem Ipsum is simply dummy text of the printing and typesetting industry.</p></div>
  <div class="ph" style="left:582px;top:1242px;width:36px;height:36px;border:2px solid #fff;border-radius:50%"></div>

  <div class="diamond" style="left:781px;top:997px;background:linear-gradient(135deg,#3c3c3e,#1b1b1d);outline:1px solid #777" role="img" aria-label="Industrial plant interior, dark tinted"></div>
  <div class="diamond-text" style="left:789px;top:1105px"><h3>Industrial<br>Electrical Services</h3><p>Lorem Ipsum is simply dummy text of the printing and typesetting industry.</p></div>
</section>

<section class="about">
  <div class="ph" style="left:0;top:1385px;width:1200px;height:655px;background:var(--grey)"></div>
  <svg class="ph" style="left:0;top:1385px" width="1200" height="110"><polygon points="580,52 1200,0 1200,92" fill="#1464c8"/><polygon points="0,0 1200,0 1200,0 580,52 0,52" fill="#fff"/></svg>
  <div class="ph" role="img" aria-label="Electrician in orange hard hat testing a panel with a multimeter" style="left:0;top:1430px;width:580px;height:610px;background:linear-gradient(120deg,#d9d6d0,#e88a3a 45%,#8a8f96)"></div>
  <div class="ph" style="left:797px;top:1735px;width:305px;height:160px;background:var(--blue)"></div>
  <div class="ph" style="left:580px;top:1560px;width:517px;height:327px;background:#fff;box-shadow:0 4px 20px rgba(0,0,0,.1)"></div>
  <div class="ghost" style="left:636px;top:1585px;font-size:80px">About us</div>
  <div class="title" style="left:638px;top:1622px;font-size:37px">Our <em>Company</em></div>
  <div class="divider" style="left:648px;top:1670px"><i></i></div>
  <p class="copy" style="left:642px;top:1700px;width:410px;font-size:13.5px;line-height:23px">Lorem ipsum dolor sit amet, consectetur adipiscing elit, sed do eiusmod tempor incididunt ut labore et dolore magna aliqua. Ut enim ad minim veniam, quis nostrud exercitation Allamco laboris nisi ut aliquip ex ea commodo consequat. Duis aute irure dolor in reprehenderit in voluptate velit esse</p>
  <div class="btn-line" style="left:642px;top:1840px;width:162px;height:48px">Learn More →</div>
</section>

<section class="area">
  <div class="ghost" style="left:138px;top:2150px;font-size:80px">Location</div>
  <div class="title" style="left:138px;top:2185px;font-size:40px">Service <em>Area</em></div>
  <div class="divider" style="left:142px;top:2234px"><i></i></div>
  <p class="copy" style="left:142px;top:2262px;width:470px;font-size:15px">Lorem ipsum dolor sit amet, consectetur adipiscing elit, sed do eiusmod tempor incididunt ut labore et dolore magn</p>
  <div class="loc" style="left:142px;top:2357px"><span class="pin"></span>Central Minnesota</div>
  <div class="loc" style="left:323px;top:2357px"><span class="pin"></span>Sed ut perspiciat</div>
  <div class="loc" style="left:496px;top:2359px"><span class="pin"></span>Location Area</div>
  <div class="loc" style="left:142px;top:2408px"><span class="pin"></span>Lorem ipsum</div>
  <div class="loc" style="left:323px;top:2408px"><span class="pin"></span>Quis autem</div>
  <div class="loc" style="left:496px;top:2411px"><span class="pin"></span>Location Area</div>
  <div class="btn-line" style="left:144px;top:2468px;width:160px;height:46px">Learn More →</div>
  <div class="ph" role="img" aria-label="County map of Minnesota with service location pins" style="left:692px;top:2110px;width:418px;height:455px;background:linear-gradient(180deg,#3a1a1c,#9c1d22 60%,#c0262d)"></div>
</section>

<section class="gallery on-dark">
  <svg class="ph" style="left:0;top:2605px" width="1200" height="680"><defs><linearGradient id="gb" x1="0" y1="0" x2="1" y2="1"><stop offset="0" stop-color="#0d4a9a"/><stop offset="1" stop-color="#2a8ad6"/></linearGradient></defs><polygon points="0,0 600,60 1200,0 1200,680 0,680" fill="url(#gb)"/><polygon points="0,0 600,60 1200,0 1200,8 600,66 0,8" fill="#b3242b"/></svg>
  <div class="ph" style="left:515px;top:2660px;width:170px;height:70px;background:#14213d;clip-path:polygon(0 10%,50% 50%,100% 10%,60% 100%,40% 100%)"></div>
  <div class="ghost" style="left:440px;top:2735px;font-size:88px;color:rgba(255,255,255,.12)">Gallery</div>
  <div class="title" style="left:500px;top:2772px;font-size:40px;color:#fff">Our Gallery</div>
  <div class="divider" style="left:537px;top:2822px"><i></i></div>
  <div class="gallery-item" role="img" aria-label="Electrician working at a control panel" style="left:78px;background:linear-gradient(135deg,#3a5a8a,#d27a2a)"></div>
  <div class="gallery-item" role="img" aria-label="Technicians inspecting switchgear" style="left:348px;background:linear-gradient(135deg,#5a6a60,#c8d23a)"></div>
  <div class="gallery-item" role="img" aria-label="Electrician installing a ceiling fixture" style="left:613px;background:linear-gradient(135deg,#d8d8d8,#8a6a50)"></div>
  <div class="gallery-item" role="img" aria-label="Workers in safety vests on site" style="left:875px;background:linear-gradient(135deg,#9aa0a6,#e08a2a)"></div>
  <svg class="ph" style="left:40px;top:2975px" width="24" height="28"><path d="M18 2 6 14l12 12" stroke="#fff" stroke-width="4" fill="none"/></svg>
  <svg class="ph" style="left:1140px;top:2975px" width="24" height="28"><path d="M6 2l12 12L6 26" stroke="#fff" stroke-width="4" fill="none"/></svg>
  <div class="btn-line" style="left:497px;top:3153px;width:220px;height:50px;border-color:#fff;color:#fff">View More Gallery</div>
</section>

<section class="faqs">
  <svg class="ph" style="left:50px;top:3380px" width="525" height="455"><polygon points="131,2 394,2 523,227 394,453 131,453 2,227" fill="none" stroke="#b3242b" stroke-width="2"/><polygon points="140,16 385,16 506,227 385,438 140,438 19,227" fill="none" stroke="#1464c8" stroke-width="2"/></svg>
  <div class="ph" role="img" aria-label="Technician in blue workwear checking wiring with a tester" style="left:92px;top:3403px;width:440px;height:410px;background:linear-gradient(135deg,#6a7480,#2f5fb0 55%,#b8bcc2);clip-path:polygon(25% 0,75% 0,100% 50%,75% 100%,25% 100%,0 50%)"></div>
  <div class="ghost" style="left:600px;top:3365px;font-size:80px">FAQ</div>
  <div class="title" style="left:605px;top:3392px;font-size:38px;line-height:42px">Frequently <em>Asked<br>Questions</em></div>
  <div class="divider" style="left:608px;top:3476px"><i></i></div>
  <div class="faq" style="top:3520px">Lorem ipsum dolor sit amet, consectetur adipiscing ?<span class="chev"></span></div>
  <div class="faq" style="top:3578px">Aed do eiusmod tempor incididunt ut ?<span class="chev"></span></div>
  <div class="faq" style="top:3636px">Pbore et dolore magna aliqua ?<span class="chev"></span></div>
  <div class="faq" style="top:3694px">Ut enim ad minim veniam quis nostrud exercitation ?<span class="chev"></span></div>
  <div class="faq" style="top:3752px;border-bottom:none">Mllamco laboris nisi ut aliquip exea ?<span class="chev"></span></div>
</section>

<section class="contact on-dark">
  <svg class="ph" style="left:0;top:3870px" width="1200" height="685"><defs><linearGradient id="cb" x1="0" y1="0" x2="1" y2="0"><stop offset="0" stop-color="#a01c22"/><stop offset=".55" stop-color="#7a1418"/><stop offset="1" stop-color="#2b2b2d"/></linearGradient></defs><polygon points="0,0 1200,70 1200,685 0,685" fill="url(#cb)"/><polygon points="0,0 610,38 0,88" fill="#1464c8"/><polygon points="0,0 1200,0 1200,70" fill="#fff"/></svg>
  <div class="ph" style="left:92px;top:4055px;width:108px;height:350px;border:3px solid #fff;border-right:none"></div>
  <div class="ghost" style="left:135px;top:4090px;font-size:64px;color:rgba(255,255,255,.12)">Get in touch</div>
  <div class="title" style="left:135px;top:4105px;font-size:38px;color:#fff">Contact Us</div>
  <div class="divider" style="left:142px;top:4152px"><i></i></div>
  <p class="ph" style="left:136px;top:4183px;font-size:14px;color:#fff">Please contact us on below contact details</p>
  <svg class="ph" style="left:138px;top:4230px" width="46" height="46"><circle cx="23" cy="23" r="23" fill="#fff"/><path d="M23 11a8 8 0 0 0-8 8c0 6 8 15 8 15s8-9 8-15a8 8 0 0 0-8-8z" fill="#b3242b"/><circle cx="23" cy="19" r="3" fill="#fff"/></svg>
  <div class="ph head" style="left:200px;top:4230px;color:#fff;font-size:15px;font-family:Barlow,sans-serif;font-weight:500">Address:<br>1420 Alder Ridge Rd Lakeview, MN 55010</div>
  <svg class="ph" style="left:138px;top:4313px" width="46" height="46"><circle cx="23" cy="23" r="23" fill="#fff"/><path d="M16 13l3 0 2 5-2.5 1.5a12 12 0 0 0 6 6L26 23l5 2v3c0 1.5-1.5 3-3 3A16 16 0 0 1 13 16c0-1.5 1.5-3 3-3z" fill="#b3242b"/></svg>
  <div class="ph head" style="left:196px;top:4313px;color:#fff;font-size:15px;font-family:Barlow,sans-serif;font-weight:500">Phone Number<br><span style="font-size:18px">555 214 7730</span></div>

  <div class="ph" style="left:560px;top:4025px;width:530px;height:410px;background:#fff;border-radius:70px 0 70px 0"></div>
  <div class="ph head" style="left:605px;top:4072px;font-size:24px;color:var(--blue)">Request a <span style="color:var(--red)">Quote</span></div>
  <div class="field" style="left:605px;top:4118px;width:218px;height:42px">First Name</div>
  <div class="field" style="left:833px;top:4118px;width:218px;height:42px">Last Name</div>
  <div class="field" style="left:605px;top:4173px;width:218px;height:42px">Email address</div>
  <div class="field" style="left:833px;top:4173px;width:218px;height:42px">Phone number</div>
  <div class="field" style="left:605px;top:4228px;width:446px;height:112px">Message</div>
  <div class="ph" style="left:605px;top:4355px;width:152px;height:42px;border-radius:21px;background:var(--blue);color:#fff;font-family:'Barlow Condensed',sans-serif;font-weight:600;font-size:15px;display:flex;align-items:center;justify-content:center">SEND MESSAGE</div>
</section>

<footer class="footer">
  <div class="ph" style="left:120px;top:60px;width:230px;height:130px;display:flex;align-items:center;justify-content:center;font-family:'Barlow Condensed',sans-serif;font-weight:600;font-size:30px;text-transform:uppercase;text-align:center;line-height:1.05">Bramblecourt<br>Electric</div>
  <div class="social"><span></span><span></span><span></span><span></span></div>
  <div class="f-sep" style="left:392px"></div>
  <div class="f-sep" style="left:572px"></div>
  <div class="f-sep" style="left:822px"></div>
  <div class="f-col" style="left:415px"><h4>Navigation</h4>Company<br>Service Area<br>Services<br>Contact<br>Gallery<br>FAQs</div>
  <div class="f-col" style="left:596px"><h4>Services</h4>Commerical Electrical Services<br>Residential Electrical Services<br>Industrial Electrical Services</div>
  <div class="f-col" style="left:853px"><h4>Contact Us</h4>
    <div style="display:flex;gap:10px;line-height:17px"><span style="width:26px;height:26px;border-radius:50%;background:#fff;flex:none"></span><span>Address<br>1420 Alder Ridge Rd<br>Lakeview, MN 55010</span></div>
    <div style="display:flex;gap:10px;align-items:center;margin-top:14px"><span style="width:26px;height:26px;border-radius:50%;background:#fff;flex:none"></span><span>Phone: <b style="color:#fff">555 214 7730</b></span></div>
  </div>
  <div class="ph" style="left:0;top:350px;width:1200px;height:1px;background:#2a2a2a"></div>
  <p class="ph" style="left:0;top:368px;width:1200px;text-align:center;font-size:11px;color:#aaa">© 2022 Bramblecourt Electric. All Rights Reserved</p>
</footer>

</body>
</html>
```